Need re-design my 2 page speaker Bio sheet

I have my current speaker biot data (speaker) sheet that is a little outdated and need a new design face lift. also some ion the information needs to be updated.
I need the design in A4 size, pdf and Adove Illustrator format.
I will attach my current bio sheet in pdf format and I will also attach my logo, some of of my professional photos and image of my book.
My website for your reference: dorianmelkrt.com
I have also attached my linked QR code
My keynote topics on page 2 is totally updated and I will attach a word document that contains the new information.
Also attached is my branding colours please avoid the use of red colour.
please keep font in arial type

```html
<!DOCTYPE html>
<html lang="en">
<head>
<meta charset="utf-8">
<title>Dorian Melkert – Speaker Bio Sheet</title>
<link href="https://fonts.googleapis.com/css2?family=Arimo:wght@400;700&display=swap" rel="stylesheet">
<style>
  :root{
    --navy:#0c2756;
    --navy-deep:#081b3d;
    --blue:#1766c2;
    --sky:#bfe0f5;
    --orange:#f5a524;
    --ink:#16223a;
    --white:#ffffff;
    --gap:#e6ebf1;
  }
  *{box-sizing:border-box;margin:0;padding:0}
  html,body{width:1200px;height:3416px;overflow:hidden;background:var(--gap);font-family:"Arimo",Arial,sans-serif;color:var(--ink)}
  .sheet{position:absolute;left:0;width:1200px;overflow:hidden;background:var(--white)}
  .sheet--bio{top:0;height:1700px}
  .sheet--topics{top:1720px;height:1696px}
  .abs{position:absolute}

  /* page 1 */
  .hero-photo{left:0;top:0;width:1200px;height:820px;background:linear-gradient(135deg,#123a6e 0%,#0b2a55 45%,#2a5d8f 100%)}
  .shapes{left:0;top:0;width:1200px;height:1700px}
  .brand{right:60px;top:50px;text-align:right;color:var(--white)}
  .brand__name{font-size:54px;font-weight:400;letter-spacing:1px}
  .brand__tag{font-size:15px;font-weight:400;letter-spacing:3px;margin-top:8px;text-transform:uppercase}
  .book-mock{left:560px;top:640px;width:580px;height:360px;border-radius:6px;background:linear-gradient(120deg,#f4f6f9 0%,#d8e0ea 50%,#f0b04a 100%)}
  .section-title{left:44px;top:945px;font-size:58px;font-weight:700;color:var(--navy);letter-spacing:1px}
  .section-title::after{content:"";display:block;width:120px;height:6px;background:var(--orange);margin-top:10px}
  .bio-text{left:44px;top:1050px;width:510px;font-size:15.5px;line-height:1.55;color:var(--ink)}
  .bio-text p{margin-bottom:14px}
  .bio-side{left:610px;top:1020px;width:550px}
  .bio-side__intro{font-size:19px;line-height:1.45;color:var(--ink)}
  .bio-side__role{margin-top:22px;font-size:26px;font-weight:700;line-height:1.3;color:var(--navy)}
  .member-row{display:flex;align-items:center;gap:18px;margin-top:18px;font-size:20px;color:var(--navy)}
  .badge{width:120px;height:50px;border-radius:6px;background:var(--navy)}
  .badge--alt{background:var(--blue)}
  .contact-title{margin-top:26px;font-size:52px;font-weight:700;color:var(--blue);letter-spacing:1px}
  .contact-list{margin-top:8px;font-size:20px;font-weight:700;line-height:1.5;color:var(--navy)}

  /* page 2 */
  .speaker-photo{left:520px;top:0;width:680px;height:840px;background:linear-gradient(160deg,#1d4d86 0%,#0f3263 55%,#0a2247 100%)}
  .topic-panel{left:0;top:0;width:560px;height:840px;background:var(--navy-deep)}
  .topic-panel__title{left:44px;top:56px;width:480px;font-size:40px;font-weight:700;color:var(--white);line-height:1.15}
  .topic-panel__text{left:44px;top:170px;width:470px;font-size:15px;line-height:1.55;color:#e3ebf6}
  .topic-panel__text p{margin-bottom:12px}
  .takeaways{left:44px;top:560px;width:480px}
  .takeaways__title{font-size:40px;font-weight:700;color:var(--orange)}
  .takeaways__list{margin-top:18px;list-style:none;font-size:19px;font-weight:700;color:var(--white);line-height:1.7}
  .takeaways__list li::before{content:"•";color:var(--orange);margin-right:12px}
  .roadmap-band{left:0;top:840px;width:1200px;height:64px;background:var(--blue);color:var(--white);font-size:34px;font-weight:700;text-align:center;line-height:64px;letter-spacing:1px}
  .roadmap{left:0;top:904px;width:1200px;height:656px;background:var(--sky);padding:40px 70px 0}
  .roadmap p{font-size:22px;line-height:1.5;color:var(--navy);margin-bottom:24px;text-align:center}
  .footer{left:0;top:1560px;width:1200px;height:136px;background:var(--blue)}
  .footer__brand{left:40px;top:40px;color:var(--white);font-size:28px;font-weight:400}
  .socials{left:290px;top:46px;display:flex;gap:16px}
  .socials span{width:44px;height:44px;border-radius:50%;background:var(--white);display:block}
  .footer__title{left:470px;top:40px;font-size:52px;font-weight:700;color:var(--white);letter-spacing:1px}
  .footer__details{left:860px;top:36px;font-size:15px;line-height:1.6;color:var(--white)}
</style>
</head>
<body>

<section class="sheet sheet--bio">
  <div class="abs hero-photo" role="img" aria-label="Photo of the speaker presenting on stage with a microphone"></div>

  <svg class="abs shapes" viewBox="0 0 1200 1700" aria-hidden="true">
    <polygon points="0,840 560,720 1200,690 1200,1700 0,1700" fill="#ffffff"/>
    <polygon points="0,770 560,640 560,700 0,840" fill="#1766c2"/>
    <polygon points="0,840 560,700 560,716 0,860" fill="#f5a524"/>
    <polygon points="580,1000 1200,1000 1200,1650 580,1650" fill="#eaf3fb"/>
    <polygon points="0,1664 1200,1644 1200,1700 0,1700" fill="#0c2756"/>
    <polygon points="0,1676 700,1664 700,1676 0,1690" fill="#1766c2"/>
    <polygon points="1080,1700 1200,1650 1200,1700" fill="#f5a524"/>
  </svg>

  <div class="abs brand">
    <div class="brand__name">Dorian Melkert</div>
    <div class="brand__tag">Entrepreneur · Keynote Speaker · Author</div>
  </div>

  <div class="abs book-mock" role="img" aria-label="Book cover and phone mockups of the book Why Comfort Stalls"></div>

  <h2 class="abs section-title">BIOGRAPHY</h2>

  <div class="abs bio-text">
    <p>Dr Dorian Melkert is a keynote speaker, author and successful entrepreneur. He has a background in workplace engineering, organisational change and business management across multiple sectors, industries and nations and has decades of experience in the field.</p>
    <p>Throughout his professional career, Dr Melkert has refined his skills and experience in business management across a successful corporate career, in startups, in multiple small businesses and in property and investment, developing innovative strategies for growth.</p>
    <p>Dr Melkert holds a doctorate in Business Administration along with a Master of Business, an MBA and several other qualifications in business administration, management and accounting. He is also the founder and director of a training college for early childhood educators.</p>
    <p>As an authority on business leadership, Dr Melkert shares his knowledge of complacency and innovation, providing practical insights into the future of leadership. He helps leaders and teams break old habits, spot fresh opportunities and turn bold ideas into lasting results.</p>
  </div>

  <div class="abs bio-side">
    <p class="bio-side__intro">Dr Dorian Melkert is a sought after keynote speaker at business, academic and personal development and industry summits – internationally. His #1 Best-Selling book, “Why Comfort Stalls”, was released in 2020.</p>
    <p class="bio-side__role">Dr Dorian Melkert was the President of Speakers Guild of Australasia (SGA) for Victoria/Tasmania for 2021.</p>
    <div class="member-row">Member of <span class="badge"></span><span class="badge badge--alt"></span></div>
    <div class="member-row">Member of Curator for <span class="badge"></span></div>
    <h3 class="contact-title">CONTACT</h3>
    <div class="contact-list">
      Phone: +61 400 123 987<br>
      Email: info@dorianmelkrt.com<br>
      Website: www.dorianmelkrt.com
    </div>
  </div>
</section>

<section class="sheet sheet--topics">
  <div class="abs speaker-photo" role="img" aria-label="Photo of the speaker smiling in front of a presentation screen"></div>
  <div class="abs topic-panel"></div>

  <h2 class="abs topic-panel__title">HOW TO BECOME A PROFIT GENERATOR</h2>
  <div class="abs topic-panel__text">
    <p>Leaders who are too complacent often find themselves replaced by those who are more daring. Playing it safe won't get you very far in today's competitive business landscape. If you're like most people, you may feel stuck in a job, career or business you hate.</p>
    <p>It's easy to get comfortable and productive where you're stuck in a rut. You feel like you're not making any progress and your competition is pulling ahead.</p>
    <p>Dr Dorian Melkert is an expert on the subject of complacent leadership. He has written a #1 best-selling book on the subject, 'Why Comfort Stalls', a testament to his expertise.</p>
    <p>In this keynote, Dr Melkert shares the latest research on motivation, productivity and leadership. You will learn how to recognise complacency and apply proven strategies for growth and sustained profit.</p>
  </div>

  <div class="abs takeaways">
    <h3 class="takeaways__title">Key Take aways:</h3>
    <ul class="takeaways__list">
      <li>Recognise the complacency signals</li>
      <li>It starts and ends with you - asses and re-asses</li>
      <li>STEER your future with an unlimited IDEA</li>
    </ul>
  </div>

  <h2 class="abs roadmap-band">HOW TO CREATE PROFITABLE ROADMAPS</h2>
  <div class="abs roadmap">
    <p>Bad business ideas can be really destructive, and it's hard to know when you're actually onto something with an idea.</p>
    <p>How do you know if your business idea is any good? How do you avoid wasting time on a bad idea?</p>
    <p>Most people never turn their great ideas into successful businesses because they don't know how to create a roadmap from their idea to profitability. Other people think that if they have a good idea, it will be successful. But this isn't always the case. Without a roadmap to profitability, your great idea might not make it off the ground.</p>
    <p>Dr Dorian Melkert, in this keynote, will open up your mind on how to create feasible business ideas and pursue them to its successful fruition. He will show you how to create profitable roadmaps that help you achieve your business and lifestyle goals. In this keynote, you'll learn how to identify viable business ideas and pursue them to their successful fruition.</p>
    <p>Dr Dorian Melkert will show you how to STEER your future with an unlimited IDEA.</p>
  </div>

  <footer class="abs footer">
    <div class="abs footer__brand">Dorian Melkert</div>
    <div class="abs socials"><span></span><span></span><span></span></div>
    <div class="abs footer__title">CONTACT</div>
    <div class="abs footer__details">
      Phone: +61 400 123 987<br>
      Email: info@dorianmelkrt.com<br>
      Website: www.dorianmelkrt.com
    </div>
  </footer>
</section>

</body>
</html>
```